Book Cover Design Project - SIMPLE ART, Pre-Concepted

We already have a full design concept for the cover art. It is however in a low quality word document format. This project is to recreate existing example guideline art in as much vector art possible for great quality print production. Artistic flare is welcome. This will be for a book cover (front/back) and I want the quality to be excellent.

Art to be provided in Adobe Illustrator format. The book will be 6wide x 9high, so the artboard for the cover needs to be set up to 12.5 wide x 9 high with .125" bleeds.

Copy content for the spine: "Beneath a Copper Evening Sky Still" RL Moskowicz.

Here is a link to download the word document "template" and a new photo for the back page. I'm not sure that I like the new photo, it is possible the old one in the word document will work.

www.bluemarlinpressworks.com/uploads/QuillHavenSharedFiles.zip

I've got a fast deadline on this project because the client would like to have manufacturing completed by Christmas...which is why this is only a 2 day project. I appreciate your interest in our project.

Gordon

Try this link...seems I was missing the .zip extension which may have been causing problems.

Requirements
Must have
• Adobe Illustrator Files
CMYK color setup - no color definitions for project
Artboard Size: 12.625 wide x 9.125 high
Art Orientation: Flat image should have the back book page on the left side, front page on the right side, spine copy running down the middle.

```html
<!DOCTYPE html>
<html lang="en">
<head>
<meta charset="utf-8">
<title>Beneath a Copper Evening Sky Still — Cover</title>
<link rel="stylesheet" href="https://fonts.googleapis.com/css2?family=Comfortaa:wght@300;400;700&family=Pinyon+Script&display=swap">
<style>
  :root {
    --paper: #ffffff;
    --navy: #0b2b50;
    --navy-deep: #082443;
    --spine: #0d3a68;
    --copy-blue: #3a9bd6;
    --heading-blue: #5cc0f0;
    --white: #ffffff;
    --sky-top: #0f5590;
    --sky-mid: #3c95d2;
    --sky-low: #8fd3f3;
    --title-ink: #0d4a86;
    --crop: #9a9a9a;
  }
  * { box-sizing: border-box; margin: 0; padding: 0; }
  html, body { width: 1200px; height: 881px; overflow: hidden; background: var(--paper); }
  .canvas { position: relative; width: 1200px; height: 881px; background: var(--paper); }

  .crop-mark { position: absolute; background: var(--crop); }
  .crop-mark.h { height: 1px; width: 14px; }
  .crop-mark.v { width: 1px; height: 12px; }

  .cover {
    position: absolute; left: 26px; top: 14px; width: 1159px; height: 852px;
    background: var(--navy); font-family: "Comfortaa", sans-serif;
  }

  /* Back */
  .back { position: absolute; left: 0; top: 0; width: 551px; height: 852px; }
  .author-photo {
    position: absolute; left: 36px; top: 48px; width: 122px; height: 144px;
    border: 1px solid var(--heading-blue);
    background: linear-gradient(160deg, #1c7fc8 0%, #3aa2e0 45%, #1a3f6a 100%);
  }
  .about-lead {
    position: absolute; left: 175px; top: 43px; width: 360px;
    color: var(--copy-blue); font-size: 17px; line-height: 26px; font-weight: 300;
    text-align: justify;
  }
  .about-lead .label { color: var(--heading-blue); font-weight: 400; }
  .about-lead .name { color: var(--white); font-weight: 400; }
  .about-lead .mark {
    display: inline-block; width: 9px; height: 9px; margin-left: 10px;
    background: var(--white); border: 1px solid #d33; vertical-align: middle;
  }
  .bio {
    position: absolute; left: 40px; top: 202px; width: 500px;
    color: var(--copy-blue); font-size: 11.6px; line-height: 18.6px; font-weight: 300;
    text-align: justify;
  }
  .bio p + p { margin-top: 18px; }

  /* Spine */
  .spine {
    position: absolute; left: 551px; top: 0; width: 50px; height: 852px;
    background: var(--spine);
  }
  .spine-title {
    position: absolute; left: 50%; top: 165px;
    transform: translateX(-50%); writing-mode: vertical-rl;
    color: var(--heading-blue); font-size: 17px; letter-spacing: 0.5px;
    white-space: nowrap; font-weight: 300;
  }

  /* Front */
  .front { position: absolute; left: 601px; top: 0; width: 558px; height: 852px; }
  .sky {
    position: absolute; left: 0; top: 0; width: 558px; height: 791px;
    background:
      radial-gradient(ellipse 70% 40% at 50% 92%, rgba(230,246,255,0.85), rgba(230,246,255,0) 70%),
      radial-gradient(ellipse 60% 35% at 55% 40%, rgba(190,230,252,0.6), rgba(190,230,252,0) 70%),
      linear-gradient(180deg, var(--sky-top) 0%, var(--sky-mid) 40%, var(--sky-low) 100%);
  }
  .cross { position: absolute; left: 0; top: 0; }
  .title-word {
    position: absolute; font-family: "Pinyon Script", cursive;
    color: var(--title-ink); font-size: 34px; white-space: nowrap;
  }
  .title-top { left: 150px; top: 202px; }
  .title-left { left: 45px; top: 380px; }
  .title-right { left: 462px; top: 380px; }
  .title-bottom { left: 258px; top: 686px; }
  .imprint {
    position: absolute; left: 38px; top: 801px;
    color: var(--white); font-size: 16px; font-weight: 400;
  }
</style>
</head>
<body>
<div class="canvas">
  <span class="crop-mark h" style="left:0;top:14px"></span>
  <span class="crop-mark h" style="right:0;top:14px"></span>
  <span class="crop-mark h" style="left:0;top:866px"></span>
  <span class="crop-mark h" style="right:0;top:866px"></span>
  <span class="crop-mark v" style="left:26px;top:0"></span>
  <span class="crop-mark v" style="left:1185px;top:0"></span>
  <span class="crop-mark v" style="left:26px;bottom:0"></span>
  <span class="crop-mark v" style="left:1185px;bottom:0"></span>

  <div class="cover">
    <section class="back">
      <div class="author-photo" role="img" aria-label="Portrait photograph of the author"></div>
      <p class="about-lead"><span class="label">About the author:</span> The word of God says that " I know the plans I have for you" (Jeremiah 29:11) and that "before I formed you in the womb I knew you" (Jeremiah 1:5). These verses of scripture depict the life of <span class="name">Reuben L Moskowicz.</span><span class="mark"></span></p>
      <div class="bio">
        <p>As a litte boy Reuben was always told that he was going to be a preacher. The magnitude of this repeated statement and exactly what it entailed was not taken seriously or truly understood, at that time. It was not Reuben's plan or desire to be a preacher, and he tried to do anything and everything to avoid the talks of him becoming one. Reuben's path of life, although he believed in God, took him down the road that led him away from God. His struggles with life's events and begin an introvert kept him emotionally troubled, in a state of depression and wanting to commit suicide. Yet, as the Lord was with Jeremiah, even so was the Lord with Reuben. The Lord was to show Reuben just what it meant to have complete trust in Him and to know that He would always provide a way of an escape. Before Reuben came to the point of carrying out his plans to commit suicide, he prayed a simple prayer that God would give him a new family. At that exact moment Reuben's life began to take a new direction. He began to seek after the Lord; it became his quest to find out what it meant to be a servant of God. Because of his being an introvert, he began to write his emotions on paper in the form of poems. Those poems gave him the strength to come out of depression and began his two year journey to find God.</p>
        <p>Reuben's relationship with Jesus and salvation journey began at the age of nineteen. The poetry writing started as a therapeutic remedy for his troubled past, but developed into the psalms of Reuben because of God's grace and mercy that delivered him from despair and hopelessness.</p>
        <p>God's favor covers Reuben's life and carries him from day to day. It is written that "without me (Christ) ye can do nothing" (John 15:5). This scripture resonates in Reuben's heart. For, he truly believes that God is the author and he is just the vessel used of God. His desire is that each poem will be taken personally and become a tool used by everyone to help them on their Christian journey and to let them know that they are never alone in their experience and quest to be closer to the Lord Jesus Christ.</p>
      </div>
    </section>

    <section class="spine">
      <p class="spine-title">"BENEATH A COPPER EVENING SKY STILL" RL MOSKOWICZ</p>
    </section>

    <section class="front">
      <div class="sky" role="img" aria-label="Soft blue sky with light clouds along the bottom"></div>
      <svg class="cross" width="558" height="791" viewBox="0 0 558 791" aria-hidden="true">
        <defs>
          <linearGradient id="cross-upright" x1="0" y1="0" x2="0" y2="1">
            <stop offset="0" stop-color="#29a6e6"/>
            <stop offset="0.55" stop-color="#1f8fd6" stop-opacity="0.9"/>
            <stop offset="1" stop-color="#9fdcf6" stop-opacity="0"/>
          </linearGradient>
          <linearGradient id="cross-arm" x1="0" y1="0" x2="0" y2="1">
            <stop offset="0" stop-color="#3ab3ec"/>
            <stop offset="1" stop-color="#1583cf"/>
          </linearGradient>
          <linearGradient id="cross-shade" x1="0" y1="0" x2="1" y2="0">
            <stop offset="0" stop-color="#ffffff" stop-opacity="0.15"/>
            <stop offset="0.5" stop-color="#ffffff" stop-opacity="0"/>
            <stop offset="1" stop-color="#003a70" stop-opacity="0.2"/>
          </linearGradient>
        </defs>
        <rect x="247" y="236" width="55" height="480" rx="6" fill="url(#cross-upright)"/>
        <rect x="247" y="236" width="55" height="480" rx="6" fill="url(#cross-shade)"/>
        <rect x="126" y="361" width="300" height="55" rx="6" fill="url(#cross-arm)"/>
      </svg>
      <span class="title-word title-top">Beneath a Copper</span>
      <span class="title-word title-left">Evening</span>
      <span class="title-word title-right">Sky</span>
      <span class="title-word title-bottom">Still</span>
      <p class="imprint">A Compliation of poems&nbsp; by RL Moskowicz</p>
    </section>
  </div>
</div>
</body>
</html>
```